Willow Glow & Laser - Business Banner with Brand Elements

Design:
• We would like to get a creative design for a wide banner that will go outside our medical spa clinic location. We need a designer to make a simple yet colorful and high-quality design layout. We want this banner to be eye-catching and to communicate the services we offer at our business: Laser Hair Removal | Velonix | Lip Filler.

Requirements:
• We would like the banner to include our companies information which is the following:

Logo
“Refresh Your Skin”
Laser Hair Removal | Velonix | Lip Filler
(555) 287-1936
www.WillowGlowLaser.com

Colors:
• Our business colors are orange, a hint of black and white, but mostly peach/orange tones. (Orange: #f78f20 , White: #ffffff)

Fonts:
• Josefins Sans Bold & Lato

Content and images can be located here:
https://files.cloudvaultshare.com/folders/7tQmZ2xVbR9kLpN4sW8yH3cD6fJ1gA0eU?usp=sharing

The following will give you an idea of our brand presentation:
• Our website is: www.WillowGlowLaser.com
• Our Instagram; @willowglowlaser
• Our Facebook: www.socialpagehub.com/willowglowlaser

Target Market(s)
• Women 25 - 45

Industry/Entity Type
• Beauty

```html
<!DOCTYPE html>
<html lang="en">
<head>
<meta charset="utf-8">
<title>Willow Glow &amp; Laser – Banner Options</title>
<link rel="stylesheet" href="https://fonts.googleapis.com/css2?family=Josefin+Sans:wght@400;700&family=Montserrat:wght@800&display=swap">
<style>
  :root {
    --orange: #f78f20;
    --orange-deep: #e97d12;
    --white: #ffffff;
    --ink: #3a3632;
    --board-light: #8c8c8c;
    --board-dark: #2c2c2c;
  }
  * { margin: 0; padding: 0; box-sizing: border-box; }
  html, body { width: 824px; height: 1200px; overflow: hidden; }
  body {
    position: relative;
    background: linear-gradient(160deg, var(--board-light) 0%, #5e5e5e 45%, var(--board-dark) 100%);
    font-family: "Josefin Sans", sans-serif;
  }
  .defs-store { position: absolute; width: 0; height: 0; }
  .option-label {
    position: absolute;
    left: 0;
    width: 824px;
    text-align: center;
    font-family: "Montserrat", sans-serif;
    font-weight: 800;
    font-size: 31px;
    line-height: 1;
    letter-spacing: 0.5px;
    color: var(--white);
  }
  .banner {
    position: absolute;
    left: 102px;
    width: 619px;
    height: 232px;
    display: block;
  }
  .headline-script { font-family: "Josefin Sans", sans-serif; font-weight: 400; fill: var(--white); }
  .headline-caps { font-family: "Josefin Sans", sans-serif; font-weight: 700; fill: var(--white); }
  .service-text { font-family: "Josefin Sans", sans-serif; font-weight: 700; fill: var(--ink); }
  .phone-text { font-family: "Josefin Sans", sans-serif; font-weight: 700; fill: var(--ink); }
  .brand-name { font-family: "Josefin Sans", sans-serif; font-weight: 700; fill: #231f1c; }
</style>
</head>
<body>

<svg class="defs-store" aria-hidden="true">
  <defs>
    <linearGradient id="beach-a" x1="0" y1="0" x2="0" y2="1">
      <stop offset="0" stop-color="#6cc3df"/>
      <stop offset="0.42" stop-color="#a9dcea"/>
      <stop offset="0.5" stop-color="#4fb3bd"/>
      <stop offset="0.62" stop-color="#e4f1f1"/>
      <stop offset="1" stop-color="#f1ebe2"/>
    </linearGradient>
    <linearGradient id="beach-b" x1="0" y1="0" x2="0" y2="1">
      <stop offset="0" stop-color="#5ecfcf"/>
      <stop offset="0.4" stop-color="#a9e2e0"/>
      <stop offset="0.5" stop-color="#3fa9ad"/>
      <stop offset="0.7" stop-color="#c7e8e4"/>
      <stop offset="1" stop-color="#eaf3ef"/>
    </linearGradient>
    <linearGradient id="beach-c" x1="0" y1="0" x2="0" y2="1">
      <stop offset="0" stop-color="#8ccbe6"/>
      <stop offset="0.3" stop-color="#cfe9f3"/>
      <stop offset="0.38" stop-color="#3ea4ad"/>
      <stop offset="0.55" stop-color="#e7f2f2"/>
      <stop offset="1" stop-color="#f2ece4"/>
    </linearGradient>
    <linearGradient id="beach-d" x1="0" y1="0" x2="0" y2="1">
      <stop offset="0" stop-color="#e9f3f6"/>
      <stop offset="0.3" stop-color="#cfe8ee"/>
      <stop offset="0.42" stop-color="#5fb4bd"/>
      <stop offset="0.6" stop-color="#e6f0ef"/>
      <stop offset="1" stop-color="#efe9e1"/>
    </linearGradient>

    <path id="photo-shape" d="M397,0 H1199 V230 C1060,208 960,250 860,312 C770,366 650,392 566,362 C504,338 482,300 480,240 C478,170 506,112 476,62 C456,28 426,10 397,0 Z"/>

    <g id="banner-back">
      <rect width="1199" height="449" fill="var(--orange)"/>
      <use href="#photo-shape" fill="none" stroke="var(--orange-deep)" stroke-width="28"/>
    </g>

    <g id="banner-front">
      <path d="M520,449 C690,428 840,372 950,312 C1050,258 1130,236 1199,246 V449 Z" fill="var(--orange-deep)"/>
      <path d="M540,449 C700,430 850,378 958,320 C1055,268 1132,248 1199,256 V449 Z" fill="var(--white)"/>

      <text class="headline-script" x="48" y="135" font-size="118" textLength="386" lengthAdjust="spacingAndGlyphs">Refresh</text>
      <text class="headline-caps" x="52" y="203" font-size="74" textLength="382" lengthAdjust="spacingAndGlyphs">YOUR SKIN</text>

      <g class="service-pill">
        <rect x="50" y="238" width="392" height="48" rx="24" fill="var(--white)"/>
        <circle cx="74" cy="262" r="19" fill="var(--orange)"/>
        <text class="service-text" x="106" y="273" font-size="29" textLength="310" lengthAdjust="spacingAndGlyphs">LASER HAIR REMOVAL</text>
      </g>
      <g class="service-pill">
        <rect x="50" y="298" width="164" height="48" rx="24" fill="var(--white)"/>
        <circle cx="74" cy="322" r="19" fill="var(--orange)"/>
        <text class="service-text" x="100" y="333" font-size="29" textLength="102" lengthAdjust="spacingAndGlyphs">VELONIX</text>
      </g>
      <g class="service-pill">
        <rect x="224" y="298" width="218" height="48" rx="24" fill="var(--white)"/>
        <circle cx="248" cy="322" r="19" fill="var(--orange)"/>
        <text class="service-text" x="274" y="333" font-size="29" textLength="150" lengthAdjust="spacingAndGlyphs">LIP FILLER</text>
      </g>

      <g class="phone-line">
        <circle cx="75" cy="402" r="23" fill="none" stroke="var(--white)" stroke-width="3.5"/>
        <path d="M64,390 c3,-3 6,-3 8,0 l3,5 c1,2 0,4 -2,5 l-2,1 c2,5 5,8 10,10 l1,-2 c1,-2 3,-3 5,-2 l5,3 c3,2 3,5 0,8 l-3,2 c-4,2 -12,-1 -19,-8 c-7,-7 -10,-15 -8,-19 z" fill="var(--white)"/>
        <text class="phone-text" x="112" y="421" font-size="50" textLength="322" lengthAdjust="spacingAndGlyphs">(555) 287-1936</text>
      </g>

      <g class="social-marks">
        <circle cx="856" cy="404" r="15" fill="var(--orange)"/>
        <circle cx="897" cy="404" r="15" fill="var(--orange)"/>
      </g>

      <g class="brand-lockup">
        <circle cx="1070" cy="304" r="36" fill="var(--orange)"/>
        <text class="brand-name" x="1070" y="386" font-size="34" text-anchor="middle">Willow Glow</text>
        <text class="brand-name" x="1070" y="418" font-size="20" text-anchor="middle" letter-spacing="4">&amp; LASER</text>
      </g>
    </g>
  </defs>
</svg>

<div class="option-label" style="top:36px">OPTION- 1</div>
<svg class="banner" style="top:71px" viewBox="0 0 1199 449">
  <use href="#banner-back"/>
  <g role="img" aria-label="Photo: smiling woman in a straw sun hat on a sunny beach">
    <use href="#photo-shape" fill="url(#beach-a)"/>
  </g>
  <use href="#banner-front"/>
</svg>

<div class="option-label" style="top:317px">OPTION- 2</div>
<svg class="banner" style="top:352px" viewBox="0 0 1199 449">
  <use href="#banner-back"/>
  <g role="img" aria-label="Photo: woman in a striped bikini top with windswept hair by the sea">
    <use href="#photo-shape" fill="url(#beach-b)"/>
  </g>
  <use href="#banner-front"/>
</svg>

<div class="option-label" style="top:598px">OPTION- 3</div>
<svg class="banner" style="top:634px" viewBox="0 0 1199 449">
  <use href="#banner-back"/>
  <g role="img" aria-label="Photo: laughing woman in a white knit top on a bright beach">
    <use href="#photo-shape" fill="url(#beach-c)"/>
  </g>
  <use href="#banner-front"/>
</svg>

<div class="option-label" style="top:879px">OPTION- 4</div>
<svg class="banner" style="top:915px" viewBox="0 0 1199 449">
  <use href="#banner-back"/>
  <g role="img" aria-label="Photo: smiling woman with windblown hair on a hazy beach">
    <use href="#photo-shape" fill="url(#beach-d)"/>
  </g>
  <use href="#banner-front"/>
</svg>

</body>
</html>
```